Website revision

I have a current website (www.tobarwendle.example) that I need to have revised. I am building a personal brand and I want it to look very professional. I built the current site and it has a lot of the elements already in place but the design is poor.

Target Market(s)

Busy working professionals that what to get in better shape

Industry/Entity Type

Health And Wellness

Number of Pages Required

1 page

Colors
00a990
9bcb3b

Requirements
Must have
• I want it re-designed with the Lumo Theme that I currently have. I want to make sure that all of my links remain active. I just need it to look more professional to my personal brand than it is at the moment.
Nice to have
• I want to appeal to a working professional that is short on time but still wants to stay healthy and fit. I am the guy that is going to provide the solution to them.
Should not have
• I do NOT want to look like a gym or a spa. I am appealing to working professionals.

```html
<!DOCTYPE html>
<html lang="en">
<head>
<meta charset="utf-8">
<title>Tobar Wendle — Your Holistic Lifestyle Hacker</title>
<link href="https://fonts.googleapis.com/css2?family=Montserrat:wght@400;500;600;700;800&family=Open+Sans:wght@400;600&display=swap" rel="stylesheet">
<style>
:root{
  --teal:#1fae94;
  --teal-dark:#17977f;
  --green:#8dc63f;
  --ink:#2c3441;
  --ink-deep:#262d38;
  --footer-box:#252c37;
  --text:#444;
  --muted:#777;
  --light:#f4f4f4;
  --white:#fff;
}
*{box-sizing:border-box;margin:0;padding:0}
html,body{width:1200px;height:2906px;overflow:hidden}
body{position:relative;font-family:"Open Sans",sans-serif;color:var(--text);background:var(--white)}
.abs{position:absolute}

/* header */
.site-header{left:0;top:0;width:1200px;height:88px;background:var(--white);border-bottom:1px solid #e6e6e6;z-index:5}
.brand{left:235px;top:24px;display:flex;align-items:center;gap:9px}
.brand-mark{width:36px;height:36px;border-radius:50%;background:var(--teal)}
.brand-name{font-family:"Montserrat",sans-serif;font-weight:800;font-size:18px;color:var(--teal);line-height:1;white-space:nowrap}
.brand-tag{font-size:7px;letter-spacing:.4px;color:var(--teal);font-family:"Montserrat",sans-serif;font-weight:800;white-space:nowrap;margin-top:3px}
.header-divider{left:466px;top:0;width:1px;height:88px;background:#e6e6e6}
.topbar{left:467px;top:0;width:733px;height:42px;border-bottom:1px solid #e6e6e6;font-family:"Montserrat",sans-serif;font-size:11px;letter-spacing:.3px;color:#333}
.topbar span{position:absolute;top:15px;white-space:nowrap}
.topbar .sep{top:0;width:1px;height:42px;background:#e6e6e6}
.cart-badge{left:475px;top:11px;width:8px;height:8px;border-radius:50%;background:var(--teal)}
.main-nav{left:492px;top:58px;display:flex;gap:28px;font-family:"Montserrat",sans-serif;font-size:9px;color:#333;letter-spacing:.2px;white-space:nowrap}
.main-nav .active{color:var(--teal)}

/* hero */
.hero-photo{left:0;top:88px;width:1200px;height:660px;background:linear-gradient(180deg,#3a404a 0%,#2f3540 55%,#2b313b 100%)}
.hero-title{left:0;top:298px;width:1200px;text-align:center;font-family:"Montserrat",sans-serif;font-weight:700;font-size:37px;line-height:46px;color:var(--white)}
.hero-title em{font-style:normal;color:var(--teal)}
.pill{height:45px;border-radius:23px;background:var(--white);font-size:11px;color:#888;display:flex;align-items:center;padding-left:45px}
.pill svg{position:absolute;left:19px;top:14px}
.btn-send{left:816px;top:418px;width:110px;height:45px;border-radius:23px;background:var(--green);color:var(--white);font-family:"Montserrat",sans-serif;font-weight:700;font-size:13px;display:flex;align-items:center;justify-content:center}
.scroll-mouse{width:11px;height:18px;border:1.5px solid var(--white);border-radius:6px}

/* about */
.about-portrait{left:185px;top:738px;width:270px;height:402px;background:linear-gradient(180deg,#b9bfc6,#8e97a2);border-radius:120px 120px 4px 4px}
.about-title{left:470px;top:808px;width:510px;text-align:center;font-family:"Montserrat",sans-serif;font-weight:800;font-size:72px;letter-spacing:-3px;color:var(--white)}
.about-text{left:470px;top:906px;width:490px;text-align:center;font-size:13.5px;line-height:20px;color:var(--white)}
.btn-outline{left:677px;top:1015px;width:102px;height:28px;border:1.5px solid var(--white);border-radius:14px;color:var(--white);font-family:"Montserrat",sans-serif;font-size:8.5px;font-weight:700;display:flex;align-items:center;justify-content:center}

/* featured */
.section-title{font-family:"Montserrat",sans-serif;font-weight:700;font-size:19px;color:var(--ink);letter-spacing:.3px}
.video{left:235px;top:1278px;width:419px;height:262px;background:linear-gradient(135deg,#5e646d,#3c424b)}
.video-play{left:179px;top:112px;width:38px;height:30px;background:var(--teal);border-radius:3px}
.video-bar{left:0;bottom:0;width:419px;height:30px;display:flex;align-items:center;gap:10px;padding:0 12px;color:var(--white);font-size:7px}
.video-bar .track{flex:1;height:4px;background:var(--white);border-radius:2px}
.article{left:670px;width:300px;height:78px}
.article-thumb{width:128px;height:78px}
.article-date{left:145px;top:6px;font-family:"Montserrat",sans-serif;font-weight:700;font-size:8.5px;color:#222}
.article-title{left:145px;top:26px;width:160px;font-family:"Montserrat",sans-serif;font-size:8.5px;line-height:15px;color:#333}

/* lead */
.lead-photo{left:530px;top:1563px;width:670px;height:386px}
.lead-decor{left:22px;top:1675px;width:210px;height:170px;background:rgba(255,255,255,.08);border-radius:4px}
.lead-heading{left:267px;top:1677px;font-family:"Montserrat",sans-serif;font-weight:700;font-size:16.5px;line-height:19px;color:var(--white)}
.field{height:30px;background:var(--white);border:1px solid #ddd;font-size:9px;color:#888;display:flex;align-items:center;padding-left:12px}
.btn-lead{left:266px;top:1818px;width:271px;height:32px;border:2px solid var(--white);border-radius:16px;color:var(--white);font-family:"Montserrat",sans-serif;font-weight:600;font-size:13px;display:flex;align-items:center;justify-content:center}

/* stories */
.stories-title{left:0;top:1976px;width:1200px;text-align:center}
.stories-intro{left:365px;top:2010px;width:490px;text-align:center;font-size:8.5px;line-height:15px;color:#444}
.green-block{left:705px;top:2196px;width:217px;height:216px;background:var(--green)}
.story-card{left:297px;top:2092px;width:580px;height:278px;background:#ececec}
.story-photo{left:0;top:0;width:293px;height:278px;background:linear-gradient(90deg,#c9b9a5 0%,#a99a88 40%,#6c6c6c 42%,#4d4d4d 100%)}
.story-text{left:320px;top:40px;width:235px;font-size:11.5px;line-height:21.5px;color:#555}
.story-rule{left:320px;top:202px;width:235px;height:1px;background:#ccc}
.story-name{left:320px;top:225px;font-family:"Montserrat",sans-serif;font-weight:600;font-size:11.5px;color:#333}
.story-nav{left:705px;top:2372px;width:217px;height:40px;display:flex;color:var(--white);font-family:"Montserrat",sans-serif;font-weight:700;font-size:8.5px}
.story-nav div{flex:1;display:flex;align-items:center;justify-content:center;gap:8px}
.story-nav div:first-child{border-right:1px solid rgba(255,255,255,.35)}

/* footer */
.footer-brand{left:0;top:2598px;width:1200px;display:flex;justify-content:center;align-items:center;gap:12px}
.footer-brand .brand-mark{width:56px;height:56px}
.footer-brand .brand-name{font-size:30px}
.footer-brand .brand-tag{font-size:10px}
.footer-rule{left:235px;top:2663px;width:732px;height:1px;background:#444c59}
.footer-nav{left:0;top:2699px;width:1200px;display:flex;justify-content:center;font-family:"Montserrat",sans-serif;font-size:8.5px;color:var(--white)}
.footer-nav span{padding:0 14px;border-right:1px solid #555e6b}
.footer-nav span:last-child{border-right:0}
.contact-box{top:2745px;height:47px;background:var(--footer-box);display:flex;align-items:center;justify-content:center;gap:14px;color:var(--white);font-family:"Montserrat",sans-serif;font-weight:600;font-size:16px;white-space:nowrap}
.social{width:26px;height:26px;border-radius:50%;background:#161b22}
.copyright-bar{left:0;top:2856px;width:1200px;height:50px;background:var(--ink-deep);text-align:center;font-size:8.5px;color:#ccc;line-height:50px}
</style>
</head>
<body>

<svg class="abs" style="left:0;top:0" width="1200" height="2906" aria-hidden="true">
  <defs>
    <linearGradient id="tealFade" x1="0" y1="0" x2="1" y2="0">
      <stop offset="0" stop-color="#1fae94"/><stop offset="1" stop-color="#21a58d"/>
    </linearGradient>
    <linearGradient id="leadPhoto" x1="0" y1="0" x2="1" y2="1">
      <stop offset="0" stop-color="#c6c9cc"/><stop offset=".5" stop-color="#9aa0a7"/><stop offset="1" stop-color="#7c8289"/>
    </linearGradient>
  </defs>
  <rect x="0" y="88" width="1200" height="660" fill="#2f3540"/>
  <polygon points="0,725 1200,620 1200,1198 0,1108" fill="url(#tealFade)"/>
  <rect x="0" y="1880" width="1200" height="700" fill="#f4f4f4"/>
  <polygon points="0,1670 560,1617 1200,1563 1200,1948 680,1910 0,1850" fill="#1fae94"/>
  <polygon points="560,1617 1200,1563 1200,1948 680,1910" fill="url(#leadPhoto)"/>
  <polygon points="0,2560 1200,2450 1200,2906 0,2906" fill="#2c3441"/>
</svg>

<header class="abs site-header">
  <div class="abs brand">
    <span class="brand-mark"></span>
    <div><div class="brand-name">TOBAR WENDLE</div><div class="brand-tag">YOUR HOLISTIC LIFESTYLE HACKER</div></div>
  </div>
  <div class="abs header-divider"></div>
  <div class="abs topbar">
    <span style="left:24px">CALL US: 555-014-2290</span>
    <span class="sep" style="left:186px"></span>
    <span style="left:204px">EMAIL: info@twfit.example</span>
    <span class="sep" style="left:392px"></span>
    <svg class="abs" style="left:406px;top:13px" width="16" height="16" viewBox="0 0 16 16"><circle cx="7" cy="7" r="5" fill="none" stroke="#999" stroke-width="1.4"/><line x1="11" y1="11" x2="15" y2="15" stroke="#999" stroke-width="1.4"/></svg>
    <span class="sep" style="left:438px"></span>
    <svg class="abs" style="left:462px;top:13px" width="16" height="16" viewBox="0 0 16 16"><path d="M1 2h3l2 8h8l1-6H5" fill="none" stroke="#999" stroke-width="1.3"/><circle cx="7" cy="13" r="1.3" fill="#999"/><circle cx="13" cy="13" r="1.3" fill="#999"/></svg>
    <span class="abs cart-badge"></span>
  </div>
  <nav class="abs main-nav">
    <span class="active">HOME</span><span>ABOUT</span><span>COURSES &amp; PROGRAMS ⌄</span><span>BLOG</span><span>TOBAR IN THE MEDIA</span><span>CONTACT</span>
  </nav>
</header>

<section class="hero">
  <div class="abs hero-photo" role="img" aria-label="Dimmed photo of Tobar in a suit inside a gym" style="clip-path:polygon(0 0,100% 0,100% 532px,0 637px)"></div>
  <h1 class="abs hero-title">YES! SEND ME<br><em>MY HEALTHY QUICK SNACK GUIDE!</em></h1>
  <div class="abs pill" style="left:276px;top:418px;width:256px">
    <svg width="16" height="17" viewBox="0 0 16 17"><circle cx="8" cy="5" r="4" fill="#1fae94"/><path d="M0 17c0-5 4-7 8-7s8 2 8 7z" fill="#1fae94"/></svg>
    Enter your name
  </div>
  <div class="abs pill" style="left:546px;top:418px;width:256px;padding-left:50px">
    <svg width="20" height="15" viewBox="0 0 20 15"><rect width="20" height="15" rx="2" fill="#1fae94"/><path d="M1 2l9 7 9-7" fill="none" stroke="#fff" stroke-width="1.6"/></svg>
    Enter your email address
  </div>
  <div class="abs btn-send">SEND ME!</div>
  <div class="abs scroll-mouse" style="left:594px;top:600px"></div>
</section>

<section class="about">
  <div class="abs about-portrait" role="img" aria-label="Portrait of Tobar in shirt and tie with jacket over shoulder"></div>
  <h2 class="abs about-title">About Me</h2>
  <p class="abs about-text">Tobar Wendle has been a powerful contributor to the health and wellness space for over 20 years.&nbsp; As a published health author, Tobar is frequently interviewed on radio stations across the country and frequently speaks as a Keynote Speaker for various associations and corporations.</p>
  <div class="abs btn-outline">LEARN MORE</div>
  <div class="abs scroll-mouse" style="left:720px;top:1089px"></div>
</section>

<section class="featured">
  <h3 class="abs section-title" style="left:233px;top:1226px">FEATURED VIDEO</h3>
  <h3 class="abs section-title" style="left:670px;top:1226px">FEATURED ARTICLES</h3>
  <div class="abs video" role="img" aria-label="Video still of Tobar in a suit standing in a training gym">
    <div class="abs video-play"><svg style="position:absolute;left:15px;top:9px" width="10" height="12" viewBox="0 0 10 12"><path d="M0 0l10 6-10 6z" fill="#fff"/></svg></div>
    <div class="abs video-bar"><svg width="7" height="8" viewBox="0 0 7 8"><path d="M0 0l7 4-7 4z" fill="#fff"/></svg><span class="track"></span><span>3:45</span></div>
  </div>
  <div class="abs article" style="top:1279px">
    <div class="article-thumb" role="img" aria-label="Photo of fresh vegetables" style="background:linear-gradient(135deg,#6c8a3a,#b34a2e)"></div>
    <div class="abs article-date">Jun 10, 2019</div>
    <div class="abs article-title">Superfoods That You Do Not Know Are Superfoods...</div>
  </div>
  <div class="abs article" style="top:1371px">
    <div class="article-thumb" role="img" aria-label="Photo of colourful fruit" style="background:linear-gradient(135deg,#b8203a,#5a4c8a 50%,#d77a2a)"></div>
    <div class="abs article-date">May 27, 2019</div>
    <div class="abs article-title">Eat Less Calories &amp; Lose Weight With This Simple Trick...</div>
  </div>
  <div class="abs article" style="top:1463px">
    <div class="article-thumb" role="img" aria-label="Photo of a fraying rope against a blue background" style="background:linear-gradient(135deg,#1a2a7a,#2e3fa0)"></div>
    <div class="abs article-date">May 20, 2019</div>
    <div class="abs article-title">The Hot Mess Inside Your Brain Is Screwing You Over Big Time...</div>
  </div>
</section>

<section class="lead">
  <div class="abs lead-photo" role="img" aria-label="Snack guide book cover and Tobar working on a laptop in a gym" style="clip-path:polygon(30px 54px,670px 0,670px 386px,150px 347px)"></div>
  <div class="abs lead-decor" role="img" aria-label="Faint program emblem"></div>
  <div class="abs lead-heading">Yes!&nbsp; Send Me My Healthy<br>Quick Snack Guide!</div>
  <div class="abs field" style="left:266px;top:1732px;width:131px">First Name</div>
  <div class="abs field" style="left:405px;top:1732px;width:131px">First Name</div>
  <div class="abs field" style="left:266px;top:1772px;width:270px">Enter your email</div>
  <div class="abs btn-lead">Send Me The Snack Guide NOW!</div>
</section>

<section class="stories">
  <h3 class="abs section-title stories-title">A FEW OF MY SUCCESS STORIES...</h3>
  <p class="abs stories-intro">I have personally coached hundreds of personal clients, corporate executives and corporations during my 20 year career in fitness and nutrition. I own a Personal Training Gym called Evergreen Fitness where I train my trainers how to use my proven lifestyle change systems. I have had the privilege of helping my clientele not only lose weight but live a holistically sustainable lifestyle of health and fitness.</p>
  <div class="abs green-block"></div>
  <div class="abs story-card">
    <div class="abs story-photo" role="img" aria-label="Before and after photos of client Daniel"></div>
    <p class="abs story-text">Daniel is an Orthodontist that owns his own business, has 6 kids and is heavily involved in his church and enjoys biking. I was fortunate enough to help Daniel understand how to incorporate weight training, food prep and sleep hygiene and more personal time into his hectic lifestyle.</p>
    <div class="abs story-rule"></div>
    <div class="abs story-name">Daniel Marsh</div>
  </div>
  <div class="abs story-nav">
    <div><svg width="22" height="8" viewBox="0 0 22 8"><path d="M22 4H1M5 0L1 4l4 4" fill="none" stroke="#fff"/></svg>Prev</div>
    <div>Next<svg width="22" height="8" viewBox="0 0 22 8"><path d="M0 4h21M17 0l4 4-4 4" fill="none" stroke="#fff"/></svg></div>
  </div>
</section>

<footer>
  <div class="abs footer-brand">
    <span class="brand-mark"></span>
    <div><div class="brand-name">TOBAR WENDLE</div><div class="brand-tag">YOUR HOLISTIC LIFESTYLE HACKER</div></div>
  </div>
  <div class="abs footer-rule"></div>
  <nav class="abs footer-nav"><span>HOME</span><span>ABOUT</span><span>COURSES &amp; PROGRAMS</span><span>BLOG</span><span>TOBAR IN THE MEDIA</span><span>CONTACT</span></nav>
  <div class="abs contact-box" style="left:235px;width:231px">
    <svg width="22" height="22" viewBox="0 0 22 22"><path d="M5 2l4 4-2 3c1 3 3 5 6 6l3-2 4 4-3 3C9 20 2 13 2 5z" fill="none" stroke="#fff" stroke-width="1.4"/></svg>555-014-2290
  </div>
  <div class="abs contact-box" style="left:485px;width:231px;font-size:15px">
    <svg width="26" height="18" viewBox="0 0 26 18"><rect width="26" height="18" rx="2" fill="#fff"/><path d="M1 2l12 9 12-9" fill="none" stroke="#252c37" stroke-width="1.8"/></svg>info@twfit.example
  </div>
  <div class="abs contact-box" style="left:735px;width:232px;font-size:13px;font-weight:500;gap:8px">
    <span style="margin-right:8px">Follow Us</span><span class="social"></span><span class="social"></span><span class="social"></span><span class="social"></span>
  </div>
  <div class="abs copyright-bar">Copyright © 2019 Tobar Wendle Your Holistic Lifestyle Hacker</div>
</footer>

</body>
</html>
```